Lone Prairie Canvas & Sound Jubilee

Organization:
Lone Prairie Canvas and Sound Jubilee is a non-profit organization created by a group of anonymous donors to bring more fun, culture, and art to a small Texas town. Our mission is to promote art and music in Washington County.
The multi-day eclectic festival will feature three stages, a film, art vendors, live mural artists, and food trucks set up throughout historic downtown Brenham. The event is FREE to the public.
Goals:
We need an attractive poster to publicize the festival.
Details:
Lone Prairie Canvas and Sound Jubilee
Friday, October 14 – 16
Free admission (VIP tickets available)
Live music- 3 stages/10 bands
Film Screening
Art vendors and art walk
Live art murals
Food trucks
www.loneprairiecanvasandsoundjubilee.example
#loneprairiecanvasandsound
Requirements:
Please incorporate our festival logo attached.
Conclusion:
After selecting a poster design, we hope to continue to work with the artist to design other event materials including website splash page and rack cards using design elements from the poster.

```html
<!DOCTYPE html>
<html lang="en">
<head>
<meta charset="utf-8">
<title>Lone Prairie Canvas &amp; Sound Jubilee</title>
<link href="https://fonts.googleapis.com/css2?family=Open+Sans:wght@700;800&family=Oswald:wght@400;500;600;700&display=swap" rel="stylesheet">
<style>
  :root {
    --sky-deep: #1d4f8f;
    --sky: #2f86c4;
    --haze: #6fa7c9;
    --glow: #f0b24a;
    --sun: #f3c35a;
    --ember: #e2772a;
    --orange: #f28a1e;
    --white: #ffffff;
    --ink: #141414;
    --violet: #7a3fa0;
    --leaf: #4f9a3c;
    --rose: #d9437e;
    --teal: #2aa6b8;
  }
  * { margin: 0; padding: 0; box-sizing: border-box; }
  html, body { width: 777px; height: 1200px; overflow: hidden; background: #222; }
  .poster {
    position: relative;
    width: 777px; height: 1200px; overflow: hidden;
    font-family: 'Oswald', 'Arial Narrow', sans-serif;
    color: var(--white);
    text-align: center;
    background: linear-gradient(180deg, var(--sky-deep) 0%, var(--sky) 28%, var(--haze) 45%, #9aa69a 56%, var(--glow) 70%, var(--sun) 86%, var(--ember) 100%);
  }
  .date {
    position: absolute; top: 48px; left: 0; width: 100%;
    font-family: 'Open Sans', Arial, sans-serif;
    font-size: 21px; font-weight: 800; letter-spacing: 0.3px;
  }
  .artwork {
    position: absolute; top: 20px; left: 0; width: 777px; height: 450px;
    background:
      radial-gradient(ellipse 38% 45% at 12% 45%, rgba(79,154,60,0.85) 0%, rgba(79,154,60,0) 100%),
      radial-gradient(ellipse 30% 40% at 88% 60%, rgba(42,166,184,0.85) 0%, rgba(42,166,184,0) 100%),
      radial-gradient(ellipse 30% 35% at 22% 78%, rgba(122,63,160,0.8) 0%, rgba(122,63,160,0) 100%),
      radial-gradient(ellipse 25% 30% at 78% 18%, rgba(217,67,126,0.6) 0%, rgba(217,67,126,0) 100%),
      radial-gradient(ellipse 45% 45% at 50% 50%, rgba(255,255,255,0.3) 0%, rgba(255,255,255,0) 100%);
  }
  .festival-mark {
    position: absolute; top: 190px; left: 0; width: 100%;
    display: flex; justify-content: center; align-items: center; gap: 16px;
  }
  .mark-circle {
    width: 150px; height: 150px; border-radius: 50%; background: var(--ink); flex: none;
  }
  .festival-name {
    width: 340px; text-align: left;
    font-size: 36px; font-weight: 500; line-height: 42px; color: var(--white);
  }
  .features {
    position: absolute; top: 470px; left: 0; width: 100%;
    font-family: 'Open Sans', Arial, sans-serif;
    font-size: 17.5px; font-weight: 800; line-height: 31px; letter-spacing: 0.2px;
  }
  .admission {
    position: absolute; top: 532px; left: 0; width: 100%;
    font-family: 'Open Sans', Arial, sans-serif;
    font-size: 31px; font-weight: 800; color: var(--orange); letter-spacing: 1px;
  }
  .vip {
    position: absolute; top: 578px; left: 0; width: 100%;
    font-family: 'Open Sans', Arial, sans-serif;
    font-size: 12px; font-weight: 800; color: var(--orange);
  }
  .schedule {
    position: absolute; top: 606px; left: 0; width: 100%;
    font-size: 12.3px; font-weight: 500; line-height: 15.6px; text-transform: uppercase;
  }
  .schedule h2 {
    font-size: 15px; font-weight: 700; text-decoration: underline; line-height: 19px;
  }
  .sponsors {
    position: absolute; top: 1050px; left: 30px; width: 717px;
    display: flex; justify-content: space-between; align-items: center;
  }
  .sponsor {
    display: flex; align-items: center; gap: 5px;
    font-size: 11px; font-weight: 600; color: var(--ink); text-transform: uppercase;
  }
  .sponsor-dot { width: 16px; height: 16px; border-radius: 50%; background: var(--ink); }
  .site {
    position: absolute; top: 1098px; left: 0; width: 100%;
    font-family: 'Open Sans', Arial, sans-serif;
    font-size: 19px; font-weight: 800; color: var(--ink);
  }
  .hashtag {
    position: absolute; top: 1134px; left: 0; width: 100%;
    font-family: 'Open Sans', Arial, sans-serif;
    font-size: 18px; font-weight: 700; color: var(--ink);
  }
</style>
</head>
<body>
<main class="poster">
  <div class="artwork" role="img" aria-label="Festival logo artwork: guitar headstock surrounded by colourful flowers, butterflies, leaves and bubbles"></div>
  <p class="date">FRIDAY, OCTOBER 14 – 16, 2016</p>

  <div class="festival-mark">
    <span class="mark-circle"></span>
    <h1 class="festival-name">Lone Prairie Canvas &amp; Sound Jubilee</h1>
  </div>

  <div class="features">
    <p>LIVE MUSIC- 3 STAGES/10 BANDS :: FILM SCREENING</p>
    <p>ART VENDORS AND ART WALK :: LIVE ART MURALS :: FOOD TRUCKS</p>
  </div>

  <p class="admission">FREE ADMISSION</p>
  <p class="vip">( VIP TICKETS AVAILABLE )</p>

  <section class="schedule">
    <h2>FRIDAY - OCT. 14TH</h2>
    <p>5:30 PM - Sponsor &amp; Artist Reception</p>
    <p>7 PM - Film Screening: Wide Country</p>
    <p>8:30 PM - Music: To Be Announced @ Cedar Hollow Farm Stage</p>
    <h2>SATURDAY - OCT. 15TH</h2>
    <p>Early Morning - Mural Artists Begin Their Work in Historic Downtown Brenham</p>
    <p>11 AM - Art Village Opens @ Mill Lane Inn</p>
    <p>11 AM - Food Truck Court Opens @ Cedar Hollow Farm... Buy Your Own Food!</p>
    <p>12 PM - Music: Dana Whitlock @ Cedar Hollow Farm Stage</p>
    <p>1:00 PM - Music: Ray Solano @ Bluebonnet Creek Brewing Stage</p>
    <p>2:00 PM - Music: Prairie Ember @ Cedar Hollow Farm Stage</p>
    <p>3 PM - Music: Wes Harlan @ Bluebonnet Creek Brewing Stage</p>
    <p>3 PM - Hill Country Brew Stroll Begins Throughout Historic Downtown</p>
    <p>3 PM - Art Walk Begins Throughout Historic Downtown</p>
    <p>3:30 PM - VIP Tent Opens @ The Main Stage</p>
    <p>4 PM - Music: Lena Marsh @ The Main Stage</p>
    <p>5:00 PM - Music: Tommy Rourke @ Cedar Hollow Farm Stage</p>
    <p>6:30 PM - Music: Gravel &amp; Gold @ The Main Stage</p>
    <p>7 PM - Hill Country Brew Stroll &amp; Art Walk Closed - Art Village &amp; Food Trucks Still Open</p>
    <p>8 PM - Art Village Closed.</p>
    <p>8:30 PM - Music: Tin Porch @ The Main Stage</p>
    <h2>SUNDAY - OCT. 16TH</h2>
    <p>Early Morning - Mural Artists Complete Their Work in Historic Downtown Brenham</p>
    <p>11 AM - Art Village Opens @ Mill Lane Inn</p>
    <p>12 PM - Music: The Indigo Tracks @ Cedar Hollow Farm Stage</p>
    <p>3 PM - Art Village Closed</p>
  </section>

  <div class="sponsors">
    <span class="sponsor"><span class="sponsor-dot"></span>Cedar Hollow Farm</span>
    <span class="sponsor"><span class="sponsor-dot"></span>Side Alley Gallery</span>
    <span class="sponsor"><span class="sponsor-dot"></span>Route 9 Radio</span>
    <span class="sponsor"><span class="sponsor-dot"></span>Bluebonnet Creek</span>
    <span class="sponsor"><span class="sponsor-dot"></span>Willowmere</span>
    <span class="sponsor"><span class="sponsor-dot"></span>Saddle Ridge</span>
    <span class="sponsor"><span class="sponsor-dot"></span>Post Oak Co.</span>
  </div>

  <p class="site">WWW.LONEPRAIRIECANVASANDSOUNDJUBILEE.EXAMPLE</p>
  <p class="hashtag">#LONEPRAIRIECANVASANDSOUND</p>
</main>
</body>
</html>
```